Need a Marketing System Program Overview Flyer

Our business, Builder Momentum Network, helps General Contractors and home improvement businesses to generate high quality leads, acquire new customers, and improve their overall online presence.

The system includes a...
- High Converting Website
- SEO & Online Listings Management
- Strategic PPC Advertising
- Email Marketing and Automation
- Social Media Management & Retargeting Campaigns
- Reputation Management
- Tracking and Reporting

The Brochure or flyer needs to have a very professional and high class look that wows the potential customers when overviewing the program.

It needs to give a clear explanation of the program while simultaneously having the very best design concept that pulls the reader in.

I've attached our branding guide, logos and additional information...

Our site is currently being staged at www.ridgevantix.com/BMN

```html
<!DOCTYPE html>
<html lang="en">
<head>
<meta charset="utf-8">
<title>Builder Momentum Network – Program Overview Flyer</title>
<link href="https://fonts.googleapis.com/css2?family=Rubik:wght@400;500;700&display=swap" rel="stylesheet">
<style>
  :root{
    --backdrop:#9a9a9a;
    --slate:#5f6372;
    --gold:#c2aa6e;
    --gold-soft:#f0d584;
    --ink:#111111;
    --navy:#1f3a5c;
    --icon-fill:#3d3d3f;
    --logo-grey:#7d7f84;
    --white:#ffffff;
  }
  *{box-sizing:border-box;margin:0;padding:0}
  html,body{width:1200px;height:776px;overflow:hidden}
  body{background:var(--backdrop);font-family:"Rubik",sans-serif;position:relative}

  .page{position:absolute;top:50px;width:538px;height:697px;overflow:hidden}
  .page--cover{left:36px;background:var(--slate)}
  .page--system{left:613px;background:var(--gold-soft)}

  .cover-photo{position:absolute;left:0;top:0;width:538px;height:420px;
    background:linear-gradient(120deg,#6d4a3f 0%,#3a3638 40%,#2b2b2e 60%,#c9a17c 85%,#f0b88d 100%)}
  .cover-shapes{position:absolute;left:0;top:0}
  .cover-brand{position:absolute;left:26px;top:58px;display:flex;align-items:center;gap:8px;
    font-weight:500;font-size:17px;color:var(--logo-grey);line-height:1.1;width:190px}
  .brand-mark{width:12px;height:12px;background:var(--gold);flex:none}

  .cover-headline{position:absolute;left:0;width:538px;top:368px;text-align:center;color:var(--white);
    font-weight:700;font-size:34px;line-height:44px;letter-spacing:-.3px}
  .cover-tagline{position:absolute;left:0;width:538px;top:575px;text-align:center;color:var(--white);
    font-size:17px;line-height:21px}
  .cover-email{position:absolute;left:100px;width:408px;top:656px;text-align:center;color:var(--ink);
    font-size:11px}

  .system-card{position:absolute;left:25px;top:25px;width:488px;height:647px;background:var(--white);border-radius:10px}
  .system-brand{position:absolute;left:0;width:488px;top:48px;display:flex;justify-content:center;align-items:center;gap:10px;
    font-weight:500;font-size:26px;color:var(--logo-grey)}
  .system-brand .brand-mark{width:16px;height:16px}
  .system-title{position:absolute;left:0;width:488px;top:113px;text-align:center;font-weight:500;font-size:21px;line-height:25px;color:var(--ink)}
  .system-intro{position:absolute;left:0;width:488px;top:166px;text-align:center;font-size:15px;letter-spacing:.6px;color:var(--ink)}

  .feature{position:absolute;width:150px;text-align:center}
  .feature-icon{display:block;margin:0 auto 4px;width:62px;height:62px}
  .feature-name{color:var(--navy);font-weight:500;font-size:14px;line-height:14px}

  .system-summary{position:absolute;left:0;width:488px;top:563px;text-align:center;color:var(--ink);font-size:13.8px;line-height:17px;white-space:nowrap}
</style>
</head>
<body>

<section class="page page--cover">
  <div class="cover-photo" role="img" aria-label="Photo of hands using a smartphone at a laptop with floating digital marketing icons"></div>
  <svg class="cover-shapes" width="538" height="697" viewBox="0 0 538 697" aria-hidden="true">
    <path d="M0 0 H250 Q252 88 170 95 L0 100 Z" fill="var(--white)"/>
    <path d="M0 370 Q250 285 538 355 V697 H0 Z" fill="var(--slate)"/>
    <path d="M0 372 Q40 352 90 340 Q40 355 0 380 Z" fill="var(--gold)"/>
    <path d="M240 322 Q440 318 538 370 V384 Q440 330 240 322 Z" fill="var(--gold)"/>
    <path d="M0 635 H70 L100 697 H0 Z" fill="var(--ink)"/>
    <path d="M80 645 H538 V685 H100 Z" fill="var(--gold)"/>
    <path d="M100 685 H538 V697 H105 Z" fill="var(--ink)"/>
  </svg>
  <div class="cover-brand"><span class="brand-mark"></span>Builder Momentum Network</div>
  <h1 class="cover-headline">Are You Ready<br>To Take Your<br>Contracting Business<br>To The Next Level?</h1>
  <p class="cover-tagline">Accelerate Your Lead Generation<br>Under One Roof - BMN</p>
  <p class="cover-email">info@buildermomentum.net</p>
</section>

<section class="page page--system">
  <div class="system-card">
    <div class="system-brand"><span class="brand-mark"></span>Builder Momentum Network</div>
    <h2 class="system-title">Our Proven 8-Point Builder<br>Momentum Network</h2>
    <p class="system-intro">The system includes a...</p>

    <div class="feature" style="left:84px;top:203px">
      <svg class="feature-icon" viewBox="0 0 62 62"><circle cx="31" cy="31" r="31" fill="var(--icon-fill)"/><g fill="none" stroke="#fff" stroke-width="2"><rect x="14" y="16" width="34" height="24" rx="2"/><path d="M31 40v6M24 46h14"/><path d="M34 30l4 4 7-8"/></g></svg>
      <p class="feature-name">High Converting<br>Websites</p>
    </div>
    <div class="feature" style="left:234px;top:203px">
      <svg class="feature-icon" viewBox="0 0 62 62"><circle cx="31" cy="31" r="31" fill="var(--icon-fill)"/><g fill="none" stroke="#fff" stroke-width="2"><circle cx="28" cy="28" r="11"/><circle cx="28" cy="28" r="15" stroke-dasharray="4 3"/><path d="M38 38l9 9"/></g></svg>
      <p class="feature-name">Social Marketing &amp;<br>Brand Development</p>
    </div>

    <div class="feature" style="left:7px;top:314px">
      <svg class="feature-icon" viewBox="0 0 62 62"><circle cx="31" cy="31" r="31" fill="var(--icon-fill)"/><path d="M12 27h6l14-8v24l-14-8h-6z" fill="#fff"/><g fill="#fff"><circle cx="42" cy="18" r="5"/><circle cx="47" cy="31" r="5"/><circle cx="42" cy="44" r="5"/></g></svg>
      <p class="feature-name">SEO &amp; Listings<br>Management</p>
    </div>
    <div class="feature" style="left:169px;top:314px">
      <svg class="feature-icon" viewBox="0 0 62 62"><circle cx="31" cy="31" r="31" fill="var(--icon-fill)"/><circle cx="27" cy="26" r="12" fill="none" stroke="#fff" stroke-width="2"/><text x="27" y="31" text-anchor="middle" font-family="Rubik,sans-serif" font-size="14" fill="#fff">$</text><path d="M32 30l14 8-6 1 4 7-3 2-4-7-4 4z" fill="#fff"/></svg>
      <p class="feature-name">Pay-Per-Click<br>Advertising</p>
    </div>
    <div class="feature" style="left:339px;top:314px">
      <svg class="feature-icon" viewBox="0 0 62 62"><circle cx="31" cy="31" r="31" fill="var(--icon-fill)"/><g fill="none" stroke="#fff" stroke-width="2"><path d="M14 30h34v18H14z"/><path d="M14 30l17 11 17-11"/><path d="M22 28l8-12 8 8"/></g></svg>
      <p class="feature-name">Email Marketing<br>&amp; Automation</p>
    </div>

    <div class="feature" style="left:7px;top:425px">
      <svg class="feature-icon" viewBox="0 0 62 62"><circle cx="31" cy="31" r="31" fill="var(--icon-fill)"/><g fill="none" stroke="#fff" stroke-width="2"><circle cx="31" cy="31" r="17"/><circle cx="24" cy="31" r="3"/><circle cx="37" cy="24" r="3"/><circle cx="37" cy="38" r="3"/><path d="M27 29l7-4M27 33l7 4"/></g></svg>
      <p class="feature-name">Social Media<br>Ads &amp; Retargeting</p>
    </div>
    <div class="feature" style="left:169px;top:425px">
      <svg class="feature-icon" viewBox="0 0 62 62"><circle cx="31" cy="31" r="31" fill="var(--icon-fill)"/><circle cx="31" cy="26" r="13" fill="#fff"/><path d="M31 19l4 7-4 7-4-7z" fill="var(--icon-fill)"/><path d="M22 36l-6 12 6-2 3 5 5-12zM40 36l6 12-6-2-3 5-5-12z" fill="#fff"/></svg>
      <p class="feature-name">Reputation<br>Management</p>
    </div>
    <div class="feature" style="left:339px;top:425px">
      <svg class="feature-icon" viewBox="0 0 62 62"><circle cx="31" cy="31" r="31" fill="var(--icon-fill)"/><g fill="none" stroke="#fff" stroke-width="2"><rect x="13" y="14" width="36" height="32" rx="2"/><path d="M13 20h36"/><path d="M18 40l8-7 6 4 10-9"/></g></svg>
      <p class="feature-name">Tracking &amp;<br>Reporting</p>
    </div>

    <p class="system-summary">We Help General Contractors Implement A Results-Driven Online<br>Marketing System That Is Proven To Generate The Highest-Quality<br>Leads, Convert Those Leads Into Customers, And Ultimately...<br>Increase Your Revenue.</p>
  </div>
</section>

</body>
</html>
```